Business Card Design Project

we are a new company , see www.chatbridgeflow.com
we also have a concurrent flyer deign competition so you may also wish to enter that.
We provide live customer support services for websites.
We cater for mainly european market.
info for card:
Martin Colbrook
Director
p: +353 (0)90 517 2861
f: +353 (0)90 517 2872
m: +353 (0)86 908 4523
e: martin@chatbridgeflow.com
w: www.chatbridgeflow.com
The card does not have to use the exact colour on the website but should ahve something of the general feel of it. It should have modern corporate feel without brash coulours. we will upload the logo and card should be standard european size 85x55mm
Target Market(s)
Online business owners
Industry/Entity Type
Business
Look and feel
Each slider illustrates characteristics of the customer's brand and the style your logo design should communicate.

```html
<!DOCTYPE html>
<html lang="en">
<head>
<meta charset="utf-8">
<title>ChatBridge Flow – Business Card</title>
<link href="https://fonts.googleapis.com/css2?family=Open+Sans:wght@400;600;700&display=swap" rel="stylesheet">
<style>
  :root {
    --page-bg: #ffffff;
    --frame-line: #3a3a3a;
    --band-light: #d6d6d6;
    --band-mid: #a9a9a9;
    --band-dark: #7c7c7c;
    --blue-top: #2f86a8;
    --blue-mid: #4aa0c0;
    --blue-low: #7cc3dc;
    --blue-strip: #2b7fa0;
    --glow-soft: rgba(255, 255, 255, 0.18);
    --glow-none: rgba(255, 255, 255, 0);
    --ink-dark: #10222b;
    --ink-white: #ffffff;
    --logo-ink: #3d3d3d;
  }
  html, body {
    margin: 0;
    padding: 0;
    width: 1200px;
    height: 901px;
    overflow: hidden;
    background: var(--page-bg);
    font-family: "Open Sans", Arial, sans-serif;
  }
  .stage {
    position: relative;
    width: 1200px;
    height: 901px;
    box-sizing: border-box;
    border: 3px solid var(--frame-line);
  }
  .card {
    position: absolute;
    left: 336px;
    top: 281px;
    width: 530px;
    height: 342px;
    overflow: hidden;
    box-shadow: 0 1px 3px rgba(0,0,0,0.25);
  }
  .card__band {
    position: absolute;
    left: 0; top: 0;
    width: 100%; height: 84px;
    background: linear-gradient(90deg, var(--band-light) 0%, var(--band-mid) 55%, var(--band-dark) 100%);
  }
  .card__body {
    position: absolute;
    left: 0; top: 84px;
    width: 100%; height: 234px;
    background: linear-gradient(180deg, var(--blue-top) 0%, var(--blue-mid) 55%, var(--blue-low) 100%);
  }
  .card__strip {
    position: absolute;
    left: 0; bottom: 0;
    width: 100%; height: 24px;
    background: var(--blue-strip);
  }
  .card__ornament {
    position: absolute;
    left: 0; top: 176px;
    width: 200px; height: 166px;
    background: linear-gradient(45deg, var(--glow-soft) 0%, var(--glow-none) 75%);
  }
  .brand {
    position: absolute;
    left: 22px; top: 29px;
    font-weight: 700;
    font-size: 20px;
    letter-spacing: 0.5px;
    color: var(--logo-ink);
    display: flex;
    align-items: center;
    gap: 8px;
  }
  .brand__mark {
    width: 15px; height: 15px;
    background: var(--logo-ink);
  }
  .web {
    position: absolute;
    right: 28px; top: 35px;
    font-size: 11px;
    color: var(--ink-white);
  }
  .person {
    position: absolute;
    right: 26px; top: 136px;
    text-align: right;
    color: var(--ink-dark);
  }
  .person__name {
    font-weight: 700;
    font-size: 19px;
    line-height: 22px;
    margin: 0;
  }
  .person__role {
    font-size: 13px;
    line-height: 16px;
    letter-spacing: 2px;
    margin: 0;
  }
  .contacts {
    position: absolute;
    right: 28px; top: 222px;
    text-align: right;
    font-size: 12.5px;
    line-height: 17.5px;
    color: var(--ink-dark);
    margin: 0;
    padding: 0;
    list-style: none;
  }
  .email {
    position: absolute;
    right: 28px; top: 294px;
    font-size: 12.5px;
    color: var(--ink-white);
  }
</style>
</head>
<body>
  <div class="stage">
    <div class="card">
      <div class="card__band"></div>
      <div class="card__body"></div>
      <div class="card__strip"></div>
      <div class="card__ornament" role="img" aria-label="Soft translucent bubble decoration in light blue"></div>
      <div class="brand"><span class="brand__mark"></span>CHATBRIDGE FLOW</div>
      <div class="web">www.chatbridgeflow.com</div>
      <div class="person">
        <p class="person__name">MARTIN COLBROOK</p>
        <p class="person__role">Director</p>
      </div>
      <ul class="contacts">
        <li>p: +353 (0)90 517 2861</li>
        <li>f: +353 (0)90 517 2872</li>
        <li>m: +353 (0)86 908 4523</li>
      </ul>
      <div class="email">martin@chatbridgeflow.com</div>
    </div>
  </div>
</body>
</html>
```